Industrial automation company needs new business cards

We need a new business card designed. We have an existing logo that is very simple and are happy to consider changes to it. We have been in business for more than 10 years and our logo has some brand recognition.
We are a company of engineers and build systems for industrial automation, substation automation, power and energy monitoring and production data vertical integration. Our main clients are food manufacturers, data centers and government establishments.
Our current business cards have our name, qualifications, job title, telephone, email and web address details. We don't need our physical address on our business cards. I've attached our current logo

Industry/Entity Type

Business

Logo Text

varlo

Font styles to use
Sans Serif

Colors
6b449b

Requirements
Must have
• - double sided business cards
• - name (eg Hello There)
• - qualifications (BE Elec MIRQT)
• - job title (eg Senior Engineer)
• - telephone (eg 0412 345 678)
• - email (eg hello.there@varlo.com.au)
• - web address (eg varlo.com.au)
Nice to have
• include our target markets on the back side of the card
• - industrial automation
• - substation automation
• - power and energy monitoring
• - production data vertical integration

```html
<!DOCTYPE html>
<html lang="en">
<head>
<meta charset="utf-8">
<title>varlo business cards</title>
<link rel="stylesheet" href="https://fonts.googleapis.com/css2?family=Open+Sans:wght@400;600;700&display=swap">
<style>
  :root {
    --brand-purple: #5607c2;
    --brand-purple-deep: #4a05a8;
    --card-white: #f6f6f6;
    --ink-grey: #5d5d5d;
    --rule-grey: #8a8a8a;
    --stage: #e4e4e6;
  }
  * { box-sizing: border-box; margin: 0; padding: 0; }
  html, body { width: 1200px; height: 904px; overflow: hidden; }
  body {
    background: var(--stage);
    font-family: "Open Sans", Arial, sans-serif;
    position: relative;
  }
  .card {
    position: absolute;
    left: 250px;
    width: 700px;
    height: 400px;
    box-shadow: 0 10px 28px rgba(0,0,0,.18);
  }
  .card--front {
    top: 32px;
    background: linear-gradient(160deg, var(--brand-purple) 0%, var(--brand-purple-deep) 100%);
    color: #fff;
  }
  .card--back {
    top: 472px;
    background: linear-gradient(135deg, #ffffff 0%, var(--card-white) 60%, #e9e9e9 100%);
  }
  .wordmark {
    position: absolute;
    left: 0; right: 0;
    display: flex;
    justify-content: center;
    align-items: center;
    gap: 14px;
    font-size: 58px;
    font-weight: 400;
    letter-spacing: 1px;
    line-height: 1;
  }
  .wordmark__dot {
    width: 18px; height: 18px;
    border-radius: 50%;
  }
  .card--front .wordmark { top: 104px; color: #fff; }
  .card--front .wordmark__dot { background: #fff; }
  .card--back .wordmark { top: 96px; color: var(--brand-purple); }
  .card--back .wordmark__dot { background: var(--brand-purple); }
  .markets {
    position: absolute;
    top: 212px; left: 0; right: 0;
    list-style: none;
    text-align: center;
    font-size: 17px;
    line-height: 1.5;
    letter-spacing: .3px;
  }
  .contact-block {
    position: absolute;
    top: 248px; left: 0; right: 0;
    display: flex;
    justify-content: center;
    align-items: stretch;
  }
  .identity {
    text-align: right;
    padding-right: 22px;
    color: var(--ink-grey);
    font-size: 17px;
    line-height: 1.35;
    padding-top: 14px;
  }
  .identity__name { color: var(--brand-purple); font-weight: 700; font-size: 22px; }
  .divider { width: 1.5px; background: var(--rule-grey); }
  .details {
    list-style: none;
    padding-left: 22px;
    color: var(--ink-grey);
    font-size: 16px;
    line-height: 1.55;
  }
  .details li { display: flex; align-items: center; gap: 10px; }
  .details svg { width: 15px; height: 15px; flex: none; }
</style>
</head>
<body>
  <section class="card card--front" aria-label="Card front">
    <div class="wordmark"><span class="wordmark__dot"></span><span>varlo</span></div>
    <ul class="markets">
      <li>Industrial Automation</li>
      <li>Substation Automation</li>
      <li>Power and Energy Monitoring</li>
      <li>Production Data Vertical Integration</li>
    </ul>
  </section>

  <section class="card card--back" aria-label="Card back">
    <div class="wordmark"><span class="wordmark__dot"></span><span>varlo</span></div>
    <div class="contact-block">
      <div class="identity">
        <div><span class="identity__name">Alex Marsh</span>, BE Elec MIRQT</div>
        <div>Senior Engineer</div>
      </div>
      <div class="divider"></div>
      <ul class="details">
        <li>
          <svg viewBox="0 0 16 16" aria-hidden="true"><path fill="#5607c2" d="M3.5 1.5l2.5 2.8-1.3 1.6c.9 2 2.4 3.5 4.4 4.4l1.6-1.3 2.8 2.5-1.6 2.1C7 13.3 2.7 9 1.4 3.1z"/></svg>
          <span>0412 345 678</span>
        </li>
        <li>
          <svg viewBox="0 0 16 16" aria-hidden="true"><rect x="1" y="3" width="14" height="10" rx="1.5" fill="#5607c2"/><path d="M1.8 4l6.2 4.8L14.2 4" fill="none" stroke="#fff" stroke-width="1.3"/></svg>
          <span>hello.there@varlo.com.au</span>
        </li>
        <li>
          <svg viewBox="0 0 16 16" aria-hidden="true"><circle cx="8" cy="8" r="7" fill="#5607c2"/><g fill="none" stroke="#fff" stroke-width="1"><ellipse cx="8" cy="8" rx="3" ry="6"/><path d="M2 8h12M3 5h10M3 11h10"/></g></svg>
          <span>varlo.com.au</span>
        </li>
      </ul>
    </div>
  </section>
</body>
</html>
```